Unique Mendrix Building Bussiness Card Design

www.mendrix.com.au

Please see website for Company profile. We require a design that incorporates our logo colours and is unique in shape and style compared to all other business cards.

www.mendrix.com.au

INSPIRE US !!!
Updates

Target Market(s)

Facility managers, Building Managers, Architects

Industry/Entity Type

Business

Contact Information for Business Card

Mendrix Building Solutions
Project Manager
Dennis Harwood
0437 619 204
Sales@mendrix.com.au

Logo Text

Mendrix Building Solutions

Logo styles of interest
Abstract Logo
Requirements
Nice to have
• Card must show we are an established big business to trust.

```html
<!DOCTYPE html>
<html lang="en">
<head>
<meta charset="utf-8">
<title>Mendrix Building Solutions – Business Card</title>
<link rel="stylesheet" href="https://fonts.googleapis.com/css2?family=PT+Sans:wght@400;700&family=Oswald:wght@300;400&display=swap">
<style>
  :root {
    --stage: #f7e6ec;
    --card: #ffffff;
    --ink: #111111;
    --name-orange: #e2622a;
    --brand-red: #9b2424;
    --brand-navy: #1f4b7a;
    --skyline-deep: #ec2f62;
    --skyline-light: #f58aa4;
  }
  html, body {
    margin: 0;
    padding: 0;
    width: 1200px;
    height: 1000px;
    overflow: hidden;
    background: var(--stage);
  }
  .canvas {
    position: relative;
    width: 1200px;
    height: 1000px;
  }
  .card {
    position: absolute;
    left: 379px;
    top: 161px;
    width: 402px;
    height: 650px;
    background: var(--card);
    overflow: hidden;
    font-family: "PT Sans", Arial, sans-serif;
    text-align: center;
  }
  .brand {
    position: absolute;
    top: 222px;
    left: 0;
    width: 100%;
    top: 70px;
    display: flex;
    justify-content: center;
    align-items: center;
    gap: 10px;
  }
  .brand-mark {
    width: 22px;
    height: 22px;
    background: var(--name-orange);
  }
  .brand-name {
    font-family: "PT Sans", Arial, sans-serif;
    font-weight: 700;
    font-size: 38px;
    color: var(--brand-navy);
    letter-spacing: 0.5px;
  }
  .role {
    position: absolute;
    top: 186px;
    left: 0;
    width: 100%;
    font-size: 18px;
    color: var(--ink);
    margin: 0;
  }
  .person {
    position: absolute;
    top: 210px;
    left: 0;
    width: 100%;
    font-size: 31px;
    color: var(--name-orange);
    margin: 0;
    letter-spacing: 0.5px;
  }
  .contact {
    position: absolute;
    top: 310px;
    left: 0;
    width: 100%;
    margin: 0;
    font-family: "Oswald", "Arial Narrow", sans-serif;
    font-weight: 300;
    font-variant: small-caps;
    font-size: 27px;
    line-height: 34px;
    color: var(--brand-red);
    letter-spacing: 1.5px;
  }
  .contact span { display: block; }
  .skyline {
    position: absolute;
    left: 0;
    bottom: 0;
    width: 402px;
    height: 200px;
  }
</style>
</head>
<body>
<div class="canvas">
  <div class="card">
    <div class="brand">
      <span class="brand-mark"></span>
      <span class="brand-name">Mendrix.com.au</span>
    </div>
    <p class="role">Project Manager</p>
    <p class="person">Dennis Harwood</p>
    <p class="contact">
      <span>Mendrix Building Solutions</span>
      <span>0437 619 204</span>
      <span>Sales@mendrix.com.au</span>
    </p>
    <svg class="skyline" viewBox="0 0 402 200" role="img" aria-label="Pink-tinted photograph of a city skyline with office towers">
      <defs>
        <linearGradient id="skylineTone" x1="0" y1="0" x2="0" y2="1">
          <stop offset="0" stop-color="var(--skyline-light)" stop-opacity="0"/>
          <stop offset="0.3" stop-color="var(--skyline-light)"/>
          <stop offset="1" stop-color="var(--skyline-deep)"/>
        </linearGradient>
      </defs>
      <rect x="0" y="0" width="402" height="200" fill="url(#skylineTone)"/>
    </svg>
  </div>
</div>
</body>
</html>
```